Appraisal and Umpire Services for Property Damage Insurance Claims

I need a banner design that I can post as an advertisement on industry web pages. I would like this to be elegant and reflective of quality, integrity and professionalism.

Target Market(s)

Insurance Companies and Attorneys

Industry/Entity Type

Insurance

Contact Information for Business Card

Gordon T. Harwell
218 Mossbank Lane
PO Box 952
Clifton Park, NY 12873
gharwell@brightmeadowclaims.example
Phone: (800) 555-0148, Ext. 2761
Direct: (315) 555-0192

Logo Text

Line One: Silver Birch Claim Service, Inc. Line two: Appraisal and Umpire Services

Font styles to use
Serif
Sans Serif

Colors
0255a3
f78f20
faa54b
3176b5

Requirements
Must have
• New Logo and matching banner, business card and stationary.
• The colors must be orange and navy blue in the logo. I have selected them below.

```html
<!DOCTYPE html>
<html lang="en">
<head>
<meta charset="utf-8">
<title>Silver Birch Claim Service – Stationery Set</title>
<link href="https://fonts.googleapis.com/css2?family=Rubik:wght@500&family=Lato:wght@400;700&family=Montserrat:wght@700&family=Oswald:wght@500&family=Roboto+Condensed:wght@700&display=swap" rel="stylesheet">
<style>
:root{
  --navy:#252a64;
  --orange:#f05a28;
  --amber:#f9a23a;
  --ink:#333;
  --stage:#c8c8c8;
  --paper:#fff;
  --label:#2a2a2a;
}
*{margin:0;padding:0;box-sizing:border-box}
html,body{width:1200px;height:930px;overflow:hidden;background:var(--stage)}
.canvas{position:relative;width:1200px;height:930px;font-family:"Lato",sans-serif;color:var(--ink)}
.piece{position:absolute;background:var(--paper);box-shadow:0 1px 4px rgba(0,0,0,.25);overflow:hidden}
.piece svg.art{position:absolute;inset:0;width:100%;height:100%}
.label{position:absolute;font-family:"Roboto Condensed",sans-serif;font-weight:700;color:var(--label);font-size:14px;transform:translateX(-50%);white-space:nowrap}
.label--big{font-size:18px}
.brand{position:absolute;font-family:"Rubik",sans-serif;font-weight:500;color:var(--navy);text-transform:uppercase;white-space:nowrap;line-height:1.1}

/* letterhead */
.backsheet{position:absolute;left:116px;top:102px;width:570px;height:776px;background:var(--navy)}
.letterhead{left:29px;top:28px;width:571px;height:808px}
.letterhead__bar{position:absolute;left:0;top:0;width:100%;height:8px;background:var(--navy)}
.letterhead .brand{left:50px;top:84px;font-size:15px;width:170px;white-space:normal;letter-spacing:.5px}
.contact{position:absolute;list-style:none;font-size:11px;color:#444;white-space:nowrap}
.contact li{display:flex;align-items:center;gap:8px;height:19px}
.contact svg{width:10px;height:10px;flex:none}
.letterhead .contact{right:34px;top:58px;font-size:10.5px}
.letter__date{position:absolute;right:34px;top:228px;font-size:10.5px}
.letter__to{position:absolute;left:35px;top:241px;font-size:10.5px;line-height:21px}
.letter__body{position:absolute;left:35px;top:314px;width:502px;font-size:9.3px;line-height:15px;text-align:justify;color:#555}
.letter__body p{text-indent:26px;margin-bottom:22px}
.letter__close{position:absolute;left:35px;top:562px;font-size:9.6px;color:#555}
.signature{position:absolute;left:35px;top:596px;width:76px;height:26px;background:linear-gradient(90deg,#e8e8e8,#f4f4f4);border-radius:3px}
.letter__sign{position:absolute;left:35px;top:638px;font-size:10px;line-height:13px;color:#555}

/* envelope */
.env-front{left:736px;top:47px;width:392px;height:175px}
.env-front .brand{left:16px;top:24px;font-size:11px;width:120px;white-space:normal}
.env-front .contact{left:16px;top:108px;font-size:7px}
.env-front .contact li{height:12px;gap:5px}
.env-front .contact svg{width:6px;height:6px}
.env-back{left:736px;top:243px;width:392px;height:177px}
.env-back .brand{left:0;width:100%;text-align:center;top:106px;font-size:15px}

/* business cards */
.card{top:490px;width:203px;height:121px}
.card--front{left:723px}
.card--back{left:943px}
.card--front .brand{left:11px;top:48px;font-size:7px;width:80px;white-space:normal}
.card__divider{position:absolute;left:98px;top:28px;width:1px;height:58px;background:#ddd}
.card__info{position:absolute;left:108px;top:35px}
.card__name{font-family:"Montserrat",sans-serif;font-weight:700;font-size:6.5px;color:var(--navy)}
.card__role{font-size:5px;font-style:italic;color:#777;margin-bottom:5px}
.card__info .contact{position:static;font-size:4px}
.card__info .contact li{height:8px;gap:3px}
.card__info .contact svg{width:4px;height:4px}
.card--back .brand{left:13px;top:48px;font-size:10px;width:105px;white-space:normal}

/* banner */
.banner{left:722px;top:694px;width:424px;height:176px}
.banner .brand{left:40px;top:8px;font-size:12px;width:150px;white-space:normal;text-align:center}
.banner__title{position:absolute;right:16px;top:18px;text-align:right;color:#fff;white-space:nowrap}
.banner__title-top{font-family:"Montserrat",sans-serif;font-weight:700;font-size:15px;letter-spacing:1px;line-height:17px}
.banner__title-main{font-family:"Oswald",sans-serif;font-weight:500;font-size:25px;line-height:28px}
.banner__phone{position:absolute;left:184px;top:80px;font-family:"Montserrat",sans-serif;font-weight:700;font-size:22px;line-height:30px;color:#fff;display:flex;align-items:center;gap:7px;white-space:nowrap}
.banner__phone svg{width:18px;height:18px}
.banner .contact{left:194px;top:128px;font-size:11px;color:#fff}
.banner .contact li{height:19px;gap:6px}
</style>
</head>
<body>
<svg width="0" height="0" style="position:absolute">
  <defs>
    <linearGradient id="flame" x1="0" y1="0" x2="1" y2="0"><stop offset="0" stop-color="#f05a28"/><stop offset="1" stop-color="#f9a23a"/></linearGradient>
    <linearGradient id="flameV" x1="0" y1="0" x2="0" y2="1"><stop offset="0" stop-color="#f05a28"/><stop offset="1" stop-color="#f9a23a"/></linearGradient>
    <linearGradient id="flameD" x1="1" y1="0" x2="0" y2="1"><stop offset="0" stop-color="#f05a28"/><stop offset="1" stop-color="#f9a23a"/></linearGradient>
    <symbol id="i-pin" viewBox="0 0 10 10"><path d="M5 0a3.5 3.5 0 0 0-3.5 3.5C1.5 6 5 10 5 10s3.5-4 3.5-6.5A3.5 3.5 0 0 0 5 0zm0 5a1.4 1.4 0 1 1 0-2.8A1.4 1.4 0 0 1 5 5z" fill="currentColor"/></symbol>
    <symbol id="i-phone" viewBox="0 0 10 10"><path d="M2 0.5l1.6 2.2-1 1.1c.6 1.4 1.6 2.4 3 3l1.1-1 2.2 1.6-.9 1.9C4 9 1 6 .3 1.4z" fill="currentColor"/></symbol>
    <symbol id="i-mail" viewBox="0 0 10 10"><path d="M0 2h10v6H0z" fill="currentColor"/><path d="M0 2l5 3.5L10 2" stroke="#fff" stroke-width=".9" fill="none"/></symbol>
  </defs>
</svg>

<main class="canvas">
  <!-- Letterhead -->
  <div class="backsheet"></div>
  <section class="piece letterhead">
    <div class="letterhead__bar"></div>
    <div class="brand">Silver Birch Claim Service, Inc.</div>
    <ul class="contact">
      <li><svg style="color:var(--amber)"><use href="#i-pin"/></svg>Gordon T. Harwell</li>
      <li><svg style="color:var(--amber)"><use href="#i-phone"/></svg>(800) 555-0148</li>
      <li><svg style="color:var(--amber)"><use href="#i-mail"/></svg>gharwell@brightmeadowclaims.example</li>
    </ul>
    <div class="letter__date">Date: 21 Oct, 2018</div>
    <div class="letter__to">Your Name Here<br>Address</div>
    <div class="letter__body">
      <p>Lorem ipsum dolor sit amet, consectetur adilpiscing elit. Suspendisse condimenttum egestas tellus et viverra. Vestibulum euismod lacus eget nisi ornare, id laoreet tortor dapibus. Dones lacinia euismod diam, convallis termpus risus, Ut et felis tempor eros blandit feugiat ut non enim, In vestibulum ligula blandit magna blandit dictum. Sed maiesuada erat id mauris pretium, ehet congue felis interdum. A enean ultricies enim nec lorem vestibulim, nec commodo quam sagittis, Cras bibendum mauris, eget aliquit semper, libero ipaum ultricies nunc, euismod pelenteque orci risus amet nibh, Maecenas feuiat mi a metus conwallis pharetra.</p>
      <p>Duis porta turpis ut pulvinar hendrerit elit lorem behichila turpls, lacinia semper pures ros ac nisi, Sed consectetur ante scienrisque tortor pellentesque imperdiet. Pellentesque habitant morbi tristique senectus et netus et malesuacia fames ac turpis egetas. Quisque justo turpis, , varius ante nec, tincidunt pharetra telus. Donec non euismod est. Nuila in elit quis tellus mattis feugiat vitae vitae ut magna. Etiam at nisi quis dolor facinia hendrent placerat et risus. Vestibulum ac sapheen ut justo varius venenatis.</p>
    </div>
    <div class="letter__close">Regards</div>
    <div class="signature" role="img" aria-label="Handwritten signature"></div>
    <div class="letter__sign">Your Name Here<br>Designation Here</div>
    <svg class="art" viewBox="0 0 571 808" preserveAspectRatio="none">
      <polygon points="0,774 169,774 151,808 0,808" fill="url(#flame)"/>
      <polygon points="240,748 272,748 247,796 215,796" fill="var(--navy)"/>
      <polygon points="278,748 571,748 571,796 253,796" fill="url(#flame)"/>
      <rect x="0" y="800" width="571" height="8" fill="#fff"/>
    </svg>
  </section>
  <div class="label label--big" style="left:366px;top:888px">LETTERHEAD</div>

  <!-- Envelope -->
  <div class="label" style="left:931px;top:19px">ENVELOPE</div>
  <section class="piece env-front">
    <svg class="art" viewBox="0 0 392 175">
      <polygon points="186,69 226,69 164,168 124,168" fill="url(#flameD)"/>
      <polygon points="238,69 392,69 392,168 176,168" fill="var(--navy)"/>
      <polygon points="0,159 92,159 84,175 0,175" fill="var(--navy)"/>
      <rect x="0" y="168" width="392" height="7" fill="#fff"/>
      <rect x="190" y="102" width="150" height="49" rx="6" fill="#fff" stroke="#ccc"/>
    </svg>
    <div class="brand">Silver Birch Claim Service, Inc.</div>
    <ul class="contact">
      <li><svg style="color:var(--navy)"><use href="#i-pin"/></svg>Gordon T. Harwell</li>
      <li><svg style="color:var(--navy)"><use href="#i-phone"/></svg>(800) 555-0148</li>
      <li><svg style="color:var(--navy)"><use href="#i-mail"/></svg>gharwell@brightmeadowclaims.example</li>
    </ul>
  </section>
  <div class="label" style="left:1160px;top:127px">FRONT</div>
  <section class="piece env-back">
    <svg class="art" viewBox="0 0 392 177">
      <path d="M0 0H392L380 62Q378 71 368 71H24Q14 71 12 62Z" fill="url(#flameV)"/>
    </svg>
    <div class="brand">Silver Birch Claim Service, Inc.</div>
  </section>
  <div class="label" style="left:1162px;top:324px">BACK</div>

  <!-- Business cards -->
  <div class="label" style="left:931px;top:459px">BUSINESS CARD</div>
  <section class="piece card card--front">
    <svg class="art" viewBox="0 0 203 121">
      <polygon points="87,4 170,4 163,18 80,18" fill="url(#flame)"/>
      <polygon points="172,4 187,4 180,18 165,18" fill="var(--navy)"/>
      <polygon points="0,96 203,96 203,106 0,106" fill="var(--navy)"/>
      <polygon points="0,104 96,104 90,117 0,117" fill="var(--navy)"/>
      <polygon points="98,104 112,104 106,117 92,117" fill="url(#flame)"/>
    </svg>
    <div class="brand">Silver Birch Claim Service, Inc.</div>
    <div class="card__divider"></div>
    <div class="card__info">
      <div class="card__name">NAME GOES HERE</div>
      <div class="card__role">Designation</div>
      <ul class="contact">
        <li><svg style="color:var(--navy)"><use href="#i-pin"/></svg>Gordon T. Harwell</li>
        <li><svg style="color:var(--navy)"><use href="#i-phone"/></svg>(800) 555-0148</li>
        <li><svg style="color:var(--navy)"><use href="#i-mail"/></svg>gharwell@brightmeadowclaims.example</li>
      </ul>
    </div>
  </section>
  <section class="piece card card--back">
    <svg class="art" viewBox="0 0 203 121">
      <polygon points="159,29 181,29 134,94 112,94" fill="url(#flameD)"/>
      <polygon points="189,29 203,29 203,94 143,94" fill="var(--navy)"/>
      <polygon points="0,102 80,102 85,96 203,96 203,110 0,110" fill="var(--navy)"/>
    </svg>
    <div class="brand">Silver Birch Claim Service, Inc.</div>
  </section>
  <div class="label" style="left:823px;top:620px">FRONT</div>
  <div class="label" style="left:1044px;top:620px">BACK</div>

  <!-- Banner -->
  <div class="label" style="left:931px;top:666px">BANNER AD</div>
  <section class="piece banner">
    <svg class="art" viewBox="0 0 424 176">
      <defs>
        <linearGradient id="scene" x1="0" y1="0" x2="0" y2="1"><stop offset="0" stop-color="#e9eef2"/><stop offset=".45" stop-color="#9aa3a6"/><stop offset="1" stop-color="#6d6a62"/></linearGradient>
      </defs>
      <g role="img" aria-label="Photo of a storm-damaged house with debris and bent palm trees">
        <polygon points="0,0 252,0 152,176 0,176" fill="url(#scene)"/>
      </g>
      <polygon points="222,0 254,0 154,176 122,176" fill="#fff"/>
      <polygon points="228,0 246,0 146,176 128,176" fill="url(#flameD)"/>
      <polygon points="256,0 424,0 424,176 156,176" fill="var(--navy)"/>
      <polygon points="184,76 424,76 424,114 162,114" fill="url(#flame)"/>
    </svg>
    <div class="brand">Silver Birch Claim Service, Inc.</div>
    <div class="banner__title">
      <div class="banner__title-top">APPRAISAL AND</div>
      <div class="banner__title-main">UMPIRE SERVICES</div>
    </div>
    <div class="banner__phone"><svg style="color:#fff"><use href="#i-phone"/></svg>(800) 555-0148</div>
    <ul class="contact">
      <li><svg style="color:#fff;width:11px;height:11px"><use href="#i-pin"/></svg>Gordon T. Harwell</li>
      <li><svg style="color:#fff;width:11px;height:11px"><use href="#i-mail"/></svg>gharwell@brightmeadowclaims.example</li>
    </ul>
  </section>
</main>
</body>
</html>
```